Logistics and freight company requires website

Hi, a Cargolane Freight company which is based in the United States needs an industry standard website for its activities. We are into forwarding and courier goods from within United States and Canada. We deliver a wide range of goods from shipping of electronics to document, clothings, etc. The proposed website should be comtemporary and youthful. I require brilliant colors for the website. The website should be the basic things of a site. There should a category for shipping electronics, clothings, documents and others( stuffs not listed within the three I mentioned).

```html
<!DOCTYPE html>
<html lang="en">
<head>
<meta charset="utf-8">
<title>Cargolane Freight</title>
<link href="https://fonts.googleapis.com/css2?family=Oswald:wght@300;400;500&family=Open+Sans:ital,wght@0,400;0,600;1,400&display=swap" rel="stylesheet">
<style>
:root{
  --brand:#3366c2;
  --ink:#333333;
  --muted:#7a7a7a;
  --band:#eeeeee;
  --footer:#0c0c0c;
  --white:#ffffff;
}
*{margin:0;padding:0;box-sizing:border-box}
html,body{width:1200px;height:2233px;overflow:hidden;background:var(--white);font-family:"Open Sans",Arial,sans-serif;color:var(--ink)}
.page{position:relative;width:1200px;height:2233px}
.abs{position:absolute}

/* header */
.site-header{left:0;top:0;width:1200px;height:92px;background:var(--white)}
.brand-name{left:52px;top:22px;font-family:"Oswald",sans-serif;font-weight:400;font-size:36px;color:var(--brand);letter-spacing:-.5px;line-height:44px;text-transform:uppercase}
.main-nav{left:609px;top:0;height:92px;display:flex}
.main-nav a{display:flex;align-items:center;height:92px;padding:0 20px;font-size:12.5px;color:var(--ink);text-decoration:none;text-transform:uppercase}
.main-nav a.active{background:var(--brand);color:var(--white)}

/* hero */
.hero{left:0;top:92px;width:1200px;height:530px;background:linear-gradient(180deg,#1d5fb8 0%,#3c86d6 55%,#9aa7b3 78%,#6e6a66 100%)}
.hero-panel{left:392px;top:246px;width:808px;height:275px;background:rgba(30,32,36,.82)}
.hero-line{right:48px;font-family:"Oswald",sans-serif;color:var(--white);font-size:45px;line-height:54px;text-align:right;text-transform:uppercase;white-space:nowrap}
.hero-line.l1{top:273px;font-weight:300}
.hero-line.l2{top:328px;font-weight:500}
.hero-line.l3{top:385px;font-weight:300}
.slider-dots{left:1080px;top:478px;display:flex;gap:10px}
.slider-dots span{width:14px;height:14px;border-radius:50%;border:1.5px solid var(--white)}
.slider-dots span.on{background:var(--brand)}

/* welcome */
.welcome-rule{top:686px;height:1px;background:#dddddd}
.welcome-title{left:0;width:1200px;top:666px;text-align:center;font-family:"Oswald",sans-serif;font-weight:400;font-size:30px;color:var(--ink);text-transform:uppercase;line-height:40px}
.welcome-title em{font-style:normal;color:var(--brand)}
.welcome-text{left:110px;width:980px;top:738px;text-align:center;font-size:11.5px;line-height:21px;color:var(--muted)}
.btn{display:flex;align-items:center;justify-content:center;text-transform:uppercase}
.read-more{left:529px;top:817px;width:141px;height:47px;background:var(--brand);color:var(--white);font-size:11px}

/* categories */
.category{top:953px;width:261px;height:316px;display:flex;align-items:center;justify-content:center;font-family:"Oswald",sans-serif;font-size:30px;color:var(--white)}
.cat-electronics{left:48px;background:linear-gradient(160deg,#f89a55,#ef8540)}
.cat-appliances{left:329px;background:linear-gradient(160deg,#f3f3f3,#d9d9d9)}
.cat-clothings{left:609px;background:linear-gradient(160deg,#3ccfc7,#26b5b0)}
.cat-documents{left:890px;background:linear-gradient(160deg,#66b23c,#4f9a2c)}
.cat-bar{left:329px;top:1231px;width:261px;height:38px;background:#222222;color:var(--white);font-family:"Oswald",sans-serif;font-size:19px;gap:14px}

/* testimonials */
.testimonials{left:0;top:1328px;width:1200px;height:301px;background:var(--band)}
.quote-box{left:365px;top:1379px;width:399px;height:170px;background:var(--white)}
.quote-text{left:388px;top:1420px;width:355px;font-style:italic;font-size:11.5px;line-height:22.5px;color:#8f8f8f}
.quote-mark{left:358px;top:1352px;font-family:"Oswald",sans-serif;font-size:72px;color:#c9c9c9;line-height:1}
.avatar{left:809px;top:1385px;width:74px;height:74px;border-radius:50%;background:linear-gradient(180deg,#e9c7a8,#2b2b2b);border:3px solid var(--white)}
.client-name{left:780px;width:132px;top:1470px;text-align:center;font-weight:600;font-size:18px;color:#555555}
.client-place{left:780px;width:92px;top:1497px;text-align:center;font-size:11px;color:#999999}

/* contact */
.contact{left:0;top:1629px;width:1200px;height:527px;background:radial-gradient(ellipse at 35% 55%,#4a4a4a 0%,#333333 45%,#262626 100%)}
.contact-title{left:76px;top:1722px;font-size:27px;font-weight:400;color:var(--white);letter-spacing:.5px}
.contact-intro{left:76px;top:1783px;width:480px;font-size:11.5px;line-height:20.5px;color:var(--white)}
.contact-rule{left:76px;top:1857px;width:487px;height:1px;background:#9a9a9a}
.contact-details{left:80px;top:1881px;font-size:15px;line-height:28.4px;color:var(--white);font-style:normal}
.field{left:655px;width:487px;border:1px solid #9a9a9a;background:rgba(255,255,255,.08);color:var(--white);font-size:14px;padding:7px 14px}
.send{left:1008px;top:2077px;width:134px;height:40px;background:var(--white);color:#555555;font-size:18px;letter-spacing:1px}

/* footer */
.site-footer{left:0;top:2156px;width:1200px;height:77px;background:var(--footer)}
.copyright{left:0;width:1200px;top:2184px;text-align:center;font-size:9.5px;color:#666666}
.social{left:1002px;top:2177px;display:flex;gap:11px}
.social span{width:28px;height:28px;border:1.5px solid #d0d0d0}
.social span.fill{background:var(--brand);border-color:var(--brand)}
</style>
</head>
<body>
<div class="page">

  <header class="site-header abs">
    <div class="brand-name abs">Cargolane Freight</div>
    <nav class="main-nav abs">
      <a class="active" href="#">Home</a>
      <a href="#">About Us</a>
      <a href="#">Our Service</a>
      <a href="#">Testimonials</a>
      <a href="#">Contact Us</a>
    </nav>
  </header>

  <section class="hero abs" role="img" aria-label="Photo of a container handler lifting a shipping container at a freight yard under a blue sky"></section>
  <div class="hero-panel abs"></div>
  <div class="hero-line l1 abs">Duis aute irure dolor in reprehenderit</div>
  <div class="hero-line l2 abs">Voluptate velit esse cillum dolore</div>
  <div class="hero-line l3 abs">Eu fugiat nulla pariatur</div>
  <div class="slider-dots abs"><span class="on"></span><span></span><span></span></div>

  <div class="welcome-rule abs" style="left:48px;width:329px"></div>
  <div class="welcome-rule abs" style="left:829px;width:322px"></div>
  <h1 class="welcome-title abs">Welcome to <em>Cargolane Freight</em></h1>
  <p class="welcome-text abs">Lorem ipsum dolor sit amet, consectetur adipiscing elit, sed do eiusmod tempor incididunt ut labore et dolore magna aliqua. Ut enim ad minim veniam, quis nostrud exercitation ullamco laboris nisi ut aliquip ex ea commodo consequat. Duis aute irure dolor in reprehenderit in voluptate velit esse cillum dolore eu fugiat nulla pariatur. Excepteur sint occaecat cupidatat non proident, sunt in culpa qui officia deserunt mollit anim id est laborum.</p>
  <div class="read-more btn abs">Read More</div>

  <div class="category cat-electronics abs" role="img" aria-label="Orange-tinted photo of air conditioning units">Electronics</div>
  <div class="category cat-appliances abs" role="img" aria-label="Photo of home appliances: air conditioners, washing machines, fridges and microwaves"></div>
  <div class="cat-bar btn abs">READ MORE
    <svg width="20" height="20" viewBox="0 0 20 20"><circle cx="10" cy="10" r="8.5" fill="none" stroke="#fff" stroke-width="1.5"/><path d="M8.5 6.5 L12 10 L8.5 13.5" fill="none" stroke="#fff" stroke-width="1.8"/></svg>
  </div>
  <div class="category cat-clothings abs" role="img" aria-label="Teal-tinted photo of clothes on a rack">Clothings</div>
  <div class="category cat-documents abs" role="img" aria-label="Green-tinted photo of stacked paper documents">Documents</div>

  <section class="testimonials abs"></section>
  <svg class="abs" style="left:196px;top:1410px" width="42" height="108" viewBox="0 0 42 108"><path d="M40 2 L3 54 L40 106" fill="none" stroke="#b5b5b5" stroke-width="1.5"/></svg>
  <svg class="abs" style="left:1003px;top:1410px" width="42" height="108" viewBox="0 0 42 108"><path d="M2 2 L39 54 L2 106" fill="none" stroke="#b5b5b5" stroke-width="1.5"/></svg>
  <div class="quote-box abs"></div>
  <svg class="abs" style="left:762px;top:1420px" width="22" height="26" viewBox="0 0 22 26"><path d="M0 0 L22 2 L0 26 Z" fill="#fff"/></svg>
  <div class="quote-mark abs">&ldquo;</div>
  <p class="quote-text abs">Lorem ipsum dolor sit amet, consectetur adipiscing elit, sed do eiusmod tempor incididunt ut labore et dolore magna aliqua. Ut enim ad minim veniam, quis nostrud exercitation ullamco laboris nisi ut aliquip ex ea commodo consequat.</p>
  <div class="avatar abs" role="img" aria-label="Client portrait photo"></div>
  <div class="client-name abs">Alex Rowan</div>
  <div class="client-place abs">City &nbsp;Location</div>

  <section class="contact abs" role="img" aria-label="Dark photo of a hand tapping on a tablet"></section>
  <h2 class="contact-title abs">GET STARTED</h2>
  <p class="contact-intro abs">Lorem ipsum dolor sit amet, consectetur adipiscing elit, sed do eiusmod tempor incididunt ut labore et dolore magna aliqua. Ut enim ad minim veniam, quis nostrud exercitation ullamco laboris nisi ut aliquip ex ea commodo consequat.</p>
  <div class="contact-rule abs"></div>
  <address class="contact-details abs">
    123 Address line1, Address line 2<br>
    Country, 123456.<br>
    Freephone: +1 555 010 2030<br>
    Telephone: +1 555 010 4050<br>
    FAX: +1 555 010 6070<br>
    <br>
    E-mail: mail@cargolane.test
  </address>
  <div class="field abs" style="top:1781px;height:35px">Name</div>
  <div class="field abs" style="top:1848px;height:35px">Email id</div>
  <div class="field abs" style="top:1913px;height:35px">Phone</div>
  <div class="field abs" style="top:1973px;height:85px">Address</div>
  <div class="send btn abs">SEND</div>

  <footer class="site-footer abs"></footer>
  <div class="copyright abs">Copyright 2016 Company Name. All Rights Reserved.</div>
  <div class="social abs"><span></span><span></span><span class="fill"></span><span></span></div>

</div>
</body>
</html>
```